Private School social media templates / ads

We are a school in South Australia -around 40kms south of Adelaide. We have 2 campuses and need fresh looks for our social media advertising.

These ads need to be designed so that our team can use them and change headings as needed or images. Ideally, PSD files or InDesign files work best.

We would need you to use stock images initially so that we can then add student photos to the ads or, if you have a different suggestion we need to come up with fresh ideas to get our message across. Here is a bit of background:

A private Christian school - one campus in Morphett Vale in the south of Adelaide and our second campus in Aldinga - we are a smaller school compared to many larger ones, so our main focus of marketing is a messages along the lines of:
- Academic Excellence (see additional notes below on this topic)
- Respect and Values and Faith
- Student focused approach to teaching - smaller class sizes means no student is left behinid.

Parents give us feedback saying they like a school with good values and one that teaches respect but also is respectful. We have a strong no-bullying policy and our academics are excellent when comparing TREVOK data.

Note - Academic Excellence.
One thing I've tried to communicate is that academic excellence is not just about getting high marks, instead, it is about encouraging students to be the best they can be. So in the past headings like - Give your Child a Great Start - and similar have worked well. Also, a strong point is - At Kestrel Ridge, your child is never just a number, but a valued part of our community.

These are some starting points. One thing I'd like to encourage is creativity - almost every school uses the same old style of advertising - a pic of 1 or 2 students and a heading like - Principals Tours - book now.

We need to stand out from the crowd when we advertise our tours.

The main focus is to increase enrolment numbers. We have a good quality CRM running so all enquiries go through a Funnel System.

I've included logos and brand documents - however, we are happy to move away from the fonts and be a bit creative with colours and tones we use.

Also, I have included a series we called -Crayons and Comets - where we created tech/space-themed ads showing where students could be in the future. This campaign ran for 2 years now and we need a fresh look with this sort of impact.

Target Market(s)

Primarily female aged 25-49

Industry/Entity Type

education - private school adelaide

Font styles to use
Sans Serif
Other font styles liked:
• Roboto is currently used but open to suggestions. Do not use Mutal Feelings font.

Requirements
Must have
• brand and promote school and school principal tours
Nice to have
• In our brand guide, there are our colours, ideally using those colors and tones for design
Should not have
• no generic ad designs - what I mean is a picture of a smiling student with the heading - Principal's Tours now on

```html
<!DOCTYPE html>
<html lang="en">
<head>
<meta charset="utf-8">
<title>Kestrel Ridge Christian College – Social Ads</title>
<link rel="stylesheet" href="https://fonts.googleapis.com/css2?family=Montserrat:wght@400;500;700;800&family=Quicksand:wght@300;400;500;600&display=swap">
<style>
  :root{
    --page:#ffffff;
    --frame-red:#e8402f;
    --navy:#1a1446;
    --navy-deep:#140f3a;
    --denim:#25306e;
    --brand-blue:#1f8fd8;
    --white:#ffffff;
    --ghost:rgba(255,255,255,0.13);
    --sun:#f3c536;
    --teal:#72bfc6;
    --footer:#f3f3f3;
  }
  *{box-sizing:border-box;margin:0;padding:0}
  html,body{width:1200px;height:839px;overflow:hidden;background:var(--page)}
  .canvas{position:relative;width:1200px;height:839px}

  /* ---------- Ad one: navy ---------- */
  .ad-navy{position:absolute;left:43px;top:45px;width:533px;height:749px;background:var(--frame-red);padding:10px}
  .ad-navy .panel{position:relative;width:100%;height:100%;overflow:hidden;
    background:linear-gradient(180deg,var(--navy-deep) 0%,var(--navy) 55%,var(--denim) 100%)}
  .brand-lockup{position:absolute;left:0;right:0;display:flex;align-items:center;justify-content:center;gap:10px}
  .brand-mark{width:30px;height:30px;border-radius:50%;background:var(--brand-blue);flex:none}
  .brand-name{font-family:'Quicksand',sans-serif;font-weight:600;font-size:23px;line-height:24px;color:var(--brand-blue)}
  .ad-navy .brand-lockup{top:44px}

  .ghost-type{position:absolute;left:0;top:0;width:513px;height:729px}
  .ghost-type text{font-family:'Montserrat',sans-serif;font-weight:500;font-size:46px;
    fill:none;stroke:var(--ghost);stroke-width:1.2}

  .student-photo{position:absolute;left:70px;top:142px;width:400px;height:587px;border-radius:200px 200px 0 0;
    background:radial-gradient(ellipse 70% 60% at 50% 35%,rgba(70,80,140,0.75) 0%,rgba(55,70,130,0.55) 55%,rgba(40,50,110,0) 100%)}
  .panel-shade{position:absolute;left:0;right:0;bottom:0;height:260px;
    background:linear-gradient(180deg,rgba(26,20,70,0) 0%,rgba(26,20,70,0.6) 55%,rgba(30,35,95,0.8) 100%)}
  .headline{position:absolute;left:0;right:0;top:505px;text-align:center;font-family:'Montserrat',sans-serif;
    font-weight:800;font-size:39px;line-height:53px;color:var(--white);letter-spacing:0.5px}
  .lede{position:absolute;left:0;right:0;top:626px;text-align:center;font-family:'Montserrat',sans-serif;
    font-weight:500;font-size:18.5px;line-height:25px;color:var(--white)}

  /* ---------- Ad two: sun & teal ---------- */
  .ad-bright{position:absolute;left:625px;top:46px;width:533px;height:749px;overflow:hidden;
    background:linear-gradient(90deg,var(--sun) 0 322px,var(--teal) 322px 100%)}
  .ad-bright .title{position:absolute;left:0;right:0;top:70px;text-align:center;font-family:'Quicksand',sans-serif;
    font-weight:600;font-size:40px;line-height:46px;color:var(--white)}
  .ad-bright .tagline{position:absolute;left:0;right:0;top:126px;text-align:center;font-family:'Quicksand',sans-serif;
    font-weight:400;font-size:27px;line-height:32px;color:var(--white)}
  .child-photo{position:absolute;left:60px;top:215px;width:420px;height:440px;border-radius:210px 210px 0 0;
    background:linear-gradient(180deg,rgba(150,100,70,0.55) 0%,rgba(170,125,95,0.45) 45%,rgba(140,185,210,0.55) 80%,rgba(230,175,185,0.55) 100%)}
  .ad-bright .footer-band{position:absolute;left:0;right:0;bottom:0;height:94px;background:var(--footer)}
  .ad-bright .brand-lockup{top:655px;height:94px}
</style>
</head>
<body>
<main class="canvas">

  <section class="ad-navy" aria-label="Happy students advertisement">
    <div class="panel">
      <div class="brand-lockup">
        <span class="brand-mark"></span>
        <span class="brand-name">Kestrel Ridge<br>Christian College</span>
      </div>

      <svg class="ghost-type" viewBox="0 0 513 729" aria-hidden="true">
        <text x="6" y="279" textLength="500" lengthAdjust="spacingAndGlyphs">HAPPY STUDENTS</text>
        <text x="20" y="347" textLength="486" lengthAdjust="spacingAndGlyphs">ENJOY LEARNING</text>
        <text x="6" y="404" textLength="500" lengthAdjust="spacingAndGlyphs">HAPPY STUDENTS</text>
        <text x="20" y="470" textLength="486" lengthAdjust="spacingAndGlyphs">ENJOY LEARNING</text>
        <text x="6" y="527" textLength="500" lengthAdjust="spacingAndGlyphs">HAPPY STUDENTS</text>
        <text x="20" y="589" textLength="486" lengthAdjust="spacingAndGlyphs">ENJOY LEARNING</text>
      </svg>

      <div class="student-photo" role="img" aria-label="Photo of a smiling senior student in a denim jacket and hoodie, arms folded"></div>
      <div class="panel-shade"></div>

      <h1 class="headline">HAPPY STUDENTS<br>ENJOY LEARNING</h1>
      <p class="lede">At Kestrel Ridge you child is valued,<br>respected and cared for.</p>
    </div>
  </section>

  <section class="ad-bright" aria-label="Faith and Focus advertisement">
    <h2 class="title">Faith and Focus</h2>
    <p class="tagline">Give your child a great start!</p>
    <div class="child-photo" role="img" aria-label="Photo of a laughing young girl with curly hair and a pink backpack, surrounded by hand-drawn school doodles"></div>
    <div class="footer-band"></div>
    <div class="brand-lockup">
      <span class="brand-mark"></span>
      <span class="brand-name">Kestrel Ridge<br>Christian College</span>
    </div>
  </section>

</main>
</body>
</html>
```